IV Bag Graphic for IV Therapy Bar

Hello we are offering an IV Therapy Bar to our medical practice. We already have a logo would like a cool design label for the IV bag. We will utilize this label for social media advertising, a sticker for the saline bag and marketing material. Woukd like something unique, sharp, bold and professional. We signed up for the Social Media package so the design will need to hold and be creative.

Target Market(s)

25-35 yrs old

Requirements
Must have
• Velmora Clinical Research name and logo- Clear inference it is IV therapy
Nice to have
• Innovation- Lines to write Name - Also please give examples of the different IV therapies (Myers cocktail) etc (screenshot example of therapies is attached)
Should not have
• In the attached examples the packaging and label are black, in open.

```html
<!DOCTYPE html>
<html lang="en">
<head>
<meta charset="utf-8">
<title>Myers Cocktail Wellness Drip Label</title>
<link href="https://fonts.googleapis.com/css2?family=Montserrat:wght@400;500;700&display=swap" rel="stylesheet">
<style>
  :root {
    --backdrop: #34689b;
    --navy: #12389a;
    --navy-deep: #0a2c86;
    --sky: #d3f1fb;
    --sky-light: #eefafe;
    --cyan: #18b6ee;
    --royal: #1a56c4;
    --grey-text: #5a5f66;
    --rule: #b9bec4;
    --white: #ffffff;
  }
  * { margin: 0; padding: 0; box-sizing: border-box; }
  html, body {
    width: 1200px; height: 2346px; overflow: hidden;
    background: var(--backdrop);
    font-family: "Montserrat", sans-serif;
  }
  .label {
    position: absolute; left: 45px; top: 334px;
    width: 740px; height: 1118px;
    transform: scale(1.5); transform-origin: top left;
    background: linear-gradient(180deg, var(--sky-light) 0%, var(--sky) 60%, var(--sky) 100%);
    overflow: hidden;
    box-shadow: 0 4px 18px rgba(0,0,0,0.25);
  }
  .label__pattern {
    position: absolute; left: 230px; top: 0; width: 510px; height: 300px;
    background: radial-gradient(ellipse at 60% 40%, rgba(160,215,240,0.45), rgba(160,215,240,0) 70%);
  }
  .label__art { position: absolute; inset: 0; }
  .title {
    position: absolute; left: 80px; top: 66px;
    color: var(--navy); font-weight: 700; font-size: 66px; line-height: 66px;
    letter-spacing: 0.5px;
  }
  .tagline {
    position: absolute; left: 80px; top: 212px; width: 369px; height: 54px;
    background: linear-gradient(90deg, var(--navy) 0%, var(--navy-deep) 100%);
    color: var(--white); font-weight: 500; font-size: 38px; line-height: 54px;
    padding-left: 17px; letter-spacing: 0.5px;
  }
  .ingredients {
    position: absolute; left: 78px; top: 308px; list-style: none;
    color: var(--navy); font-size: 31px; font-weight: 400; line-height: 45.5px;
  }
  .care-icon {
    position: absolute; left: 585px; top: 395px; width: 122px; height: 128px;
    border-radius: 50%;
    background: radial-gradient(circle, rgba(18,56,154,0.18), rgba(18,56,154,0) 70%);
  }
  .seal {
    position: absolute; top: 567px; width: 100px; height: 100px; border-radius: 50%;
    border: 2px solid var(--navy); box-shadow: inset 0 0 0 5px var(--sky), inset 0 0 0 6px var(--navy);
  }
  .seal--natural { left: 77px; }
  .seal--quality { left: 207px; }
  .volume {
    position: absolute; left: 269px; top: 779px; width: 68px; height: 68px; border-radius: 50%;
    background: radial-gradient(circle at 40% 35%, #2ecbff, var(--royal));
    color: var(--white); font-size: 17px; line-height: 68px; text-align: center;
  }
  .brand {
    position: absolute; left: 490px; top: 660px; width: 230px; text-align: center;
  }
  .brand__mark {
    width: 70px; height: 70px; border-radius: 50%; margin: 0 auto 16px;
    background: var(--navy);
  }
  .brand__name {
    color: var(--navy); font-weight: 700; font-size: 22px; line-height: 26px;
  }
  .patient-fields {
    position: absolute; left: 59px; top: 960px; width: 646px;
    color: var(--grey-text); font-size: 20px;
  }
  .field { display: flex; align-items: flex-end; height: 42.5px; }
  .field__label { white-space: nowrap; padding-right: 8px; }
  .field__line { flex: 1; border-bottom: 1px dotted var(--rule); margin-bottom: 6px; }
  .lower-texture {
    position: absolute; left: 0; top: 820px; width: 740px; height: 298px;
    background: radial-gradient(ellipse at 40% 30%, rgba(200,205,212,0.25), rgba(255,255,255,0) 70%);
  }
</style>
</head>
<body>
  <div class="label">
    <div class="label__pattern" role="img" aria-label="Soft hexagonal molecule pattern"></div>

    <svg class="label__art" viewBox="0 0 740 1118" width="740" height="1118" aria-hidden="true">
      <defs>
        <linearGradient id="waveBand" x1="0" y1="0" x2="1" y2="0">
          <stop offset="0" stop-color="#0a3aa0"/>
          <stop offset="0.45" stop-color="#16c2f4"/>
          <stop offset="1" stop-color="#1a4fb8"/>
        </linearGradient>
        <linearGradient id="swoosh" x1="0" y1="0" x2="1" y2="1">
          <stop offset="0" stop-color="#16c2f4"/>
          <stop offset="1" stop-color="#0a36a0"/>
        </linearGradient>
      </defs>
      <path d="M318 77 H660 V380" fill="none" stroke="#12389a" stroke-width="3"/>
      <path d="M0 818 C190 812 300 760 400 700 C520 628 620 570 740 600 V1118 H0 Z" fill="#ffffff"/>
      <path d="M0 804 C190 800 300 735 400 676 C520 604 625 545 740 575 L740 600 C620 570 520 628 400 700 C300 760 190 818 0 818 Z" fill="url(#waveBand)"/>
      <path d="M318 708 C390 800 480 948 740 950 L740 960 C455 962 370 820 344 704 Z" fill="url(#swoosh)"/>
    </svg>

    <div class="lower-texture" role="img" aria-label="Faint molecule dot pattern"></div>

    <h1 class="title">MYERS<br>COCKTAIL</h1>
    <div class="tagline">WELLNESS DRIP</div>

    <ul class="ingredients">
      <li>+ B - COMPLEX VITAMINS</li>
      <li>+ VITAMIN B12</li>
      <li>+ MAGNEISUM</li>
      <li>+ VITAMIN C</li>
      <li>+ CALCIUM</li>
    </ul>

    <div class="care-icon" role="img" aria-label="Line icon of a heart with pulse held in a hand"></div>

    <div class="seal seal--natural"></div>
    <div class="seal seal--quality"></div>

    <div class="volume">100ml.</div>

    <div class="brand">
      <div class="brand__mark"></div>
      <div class="brand__name">VELMORA<br>CLINICAL RESEARCH</div>
    </div>

    <div class="patient-fields">
      <div class="field"><span class="field__label">PATIENT NAME :</span><span class="field__line"></span></div>
      <div class="field"><span class="field__label">PATIENT #</span><span class="field__line"></span></div>
      <div class="field"><span class="field__label">START TIME :</span><span class="field__line"></span></div>
    </div>
  </div>
</body>
</html>
```